Vellmora- plumbing service flyer

Hello,
We would like to create flyer for our plumbing company Vellmora
- we have 2 web domains
vellmora-example.hr ( official)
preuredbastanova-example.hr ( for bathroom renovation)

- we would like to create a similar Z-fold flyer ( from A4 paper) for our services
- We are sending images used on our websites. Of Course, it is allowed to put some of their own. Depending on design
- sending word with text which should go on each page. Text can be modified but in the sense of a page. The massage on a page should be as in word.
What is important to us:
- to stay in blue color
- It should be 1 page when fully open. So it looks like the complete page of information
- first/front page should be with our logo and phone number. more focus on emergency plumbing.
- back page should be about bathroom remodeling. Not necessary but would be received more points
- please don't use images of regular plumbers from Pixelgrove and similar. we don't want to use this stock's regular images as all others.

Target Market(s)

Bathroom remodeling and emergency plumbing

Industry/Entity Type

Construction-Plumbing

Colors
0054AA
0677BA
7BADD7
CADEEF
E8F1F8

Requirements
Must have
• Logo

```html
<!DOCTYPE html>
<html lang="en">
<head>
<meta charset="utf-8">
<title>Vellmora – Plumbing Service Flyer</title>
<link rel="stylesheet" href="https://fonts.googleapis.com/css2?family=Roboto:wght@400;500;700;900&family=Montserrat:wght@600;700&display=swap">
<style>
:root{
  --navy:#0b1f5c;
  --deep:#123a8f;
  --royal:#1c55b8;
  --sky:#4cc3ee;
  --sky-soft:#7bcdf2;
  --ice:#e8f1f8;
  --yellow:#fbbf1c;
  --red:#e6322b;
  --white:#ffffff;
  --page:#f4f5f7;
}
*{box-sizing:border-box;margin:0;padding:0}
html,body{width:830px;height:1200px;overflow:hidden;background:var(--page)}
body{font-family:"Roboto",Arial,sans-serif;color:var(--white)}
.flyer{position:absolute;left:15px;top:317px;width:800px;height:566px;display:flex;box-shadow:0 10px 30px rgba(0,0,0,.18)}
.panel{position:relative;width:266.67px;height:100%;overflow:hidden}

/* left panel – bathroom remodeling */
.panel--remodel{background:linear-gradient(160deg,var(--deep),var(--royal) 60%,var(--deep))}
.remodel__headline{position:absolute;left:18px;top:26px;font-weight:900;font-size:19px;line-height:1.08;text-transform:uppercase}
.remodel__headline span{color:var(--sky)}
.remodel__rule{position:absolute;left:24px;top:96px;width:92px;height:2px;background:var(--yellow)}
.remodel__services{position:absolute;left:22px;top:110px;font-family:"Montserrat",sans-serif;font-weight:700;font-size:11px;letter-spacing:2.6px;line-height:1.9}
.remodel__services .s1{color:var(--yellow)}
.remodel__services .s2{color:var(--sky)}
.remodel__photo{position:absolute;left:-40px;top:210px;width:200px;height:200px;border-radius:50%;background:linear-gradient(135deg,#3a3f44,#6b6f72 55%,#d9d6cf);border:7px solid var(--royal)}
.remodel__pipes{position:absolute;left:170px;top:170px;width:80px;height:210px;border-radius:14px;background:linear-gradient(180deg,#8a97a8,#f0b33a 60%,#8a97a8);opacity:.9}
.remodel__emergency{position:absolute;left:60px;top:420px;font-weight:700;font-size:13px;line-height:1.15}
.remodel__wave{position:absolute;left:0;top:440px;width:100%;height:90px}
.badge247{position:absolute;left:75px;top:465px;width:52px;height:52px;border-radius:50%;background:var(--sky);border:3px solid var(--white);display:flex;align-items:center;justify-content:center;font-weight:900;font-size:15px}
.remodel__mascot{position:absolute;left:150px;top:405px;width:100px;height:110px;border-radius:50%;background:radial-gradient(circle,var(--sky),var(--royal));border:3px solid var(--white)}
.remodel__url{position:absolute;left:0;right:0;bottom:14px;text-align:center;font-weight:700;font-size:13px}

/* middle panel – services */
.panel--services{background:var(--sky)}
.services__band{position:absolute;left:0;top:0;width:100%;height:82px;background:var(--yellow);display:flex;align-items:center;justify-content:center;text-align:center}
.services__title{font-family:"Montserrat",sans-serif;font-weight:700;font-size:12px;letter-spacing:3px;line-height:1.7;color:var(--navy);text-transform:uppercase}
.services__grid{position:absolute;left:10px;right:10px;top:98px;display:grid;grid-template-columns:repeat(3,1fr);row-gap:14px}
.service{display:flex;flex-direction:column;align-items:center;text-align:center;font-size:8.5px;font-weight:500;line-height:1.2;height:66px}
.service svg{width:30px;height:30px;margin-bottom:5px}
.services__grid .service--wide{grid-column:span 1}
.services__address{position:absolute;left:40px;bottom:26px;display:flex;align-items:center;gap:8px;font-size:9px;line-height:1.3}

/* right panel – front cover */
.panel--cover{background:var(--navy)}
.cover__swoosh{position:absolute;left:0;top:180px;width:100%;height:120px}
.cover__lower{position:absolute;left:0;top:235px;width:100%;height:331px;background:var(--royal)}
.cover__mascot{position:absolute;left:58px;top:30px;width:150px;height:150px;border-radius:50%;background:radial-gradient(circle,var(--sky-soft),var(--sky) 55%,var(--deep));border:4px solid var(--white)}
.cover__brand{position:absolute;left:0;right:0;top:184px;text-align:center;display:flex;justify-content:center;align-items:center;gap:8px;font-weight:900;font-size:30px;color:var(--white)}
.cover__brand i{display:block;width:12px;height:12px;border-radius:50%;background:var(--white)}
.cover__tagline{position:absolute;left:22px;top:250px;font-weight:700;font-size:20px;line-height:1.1}
.cover__tagline span{color:var(--sky)}
.cover__intro{position:absolute;left:22px;right:18px;top:300px;font-size:8.5px;text-align:center;line-height:1.3}
.cover__features{position:absolute;left:16px;right:16px;top:330px;display:flex;justify-content:space-between;align-items:center;font-size:8.5px;font-weight:700;text-align:center;line-height:1.2}
.cover__features .sep{width:2px;height:22px;background:var(--yellow)}
.cover__emergency{position:absolute;left:0;top:370px;width:100%;height:80px;background:var(--sky);padding:10px 14px 0 58px}
.cover__emergency .label{font-weight:700;font-size:10.5px;letter-spacing:.3px;color:var(--navy)}
.cover__emergency .phone{font-weight:900;font-size:27px;line-height:1.1}
.cover__phone-icon{position:absolute;left:18px;top:20px;width:30px;height:40px}
.cover__cta{position:absolute;left:60px;top:460px;width:150px;height:30px;border-radius:15px;background:var(--yellow);color:var(--navy);font-weight:900;font-size:13px;display:flex;align-items:center;justify-content:center}
.cover__url{position:absolute;left:0;right:0;bottom:22px;text-align:center;font-weight:700;font-size:13px}
</style>
</head>
<body>
<main class="flyer">

  <!-- back: bathroom remodeling -->
  <section class="panel panel--remodel">
    <h2 class="remodel__headline">Using tech to<br>facilitate your life.<br><span>Vellmora</span></h2>
    <div class="remodel__rule"></div>
    <ul class="remodel__services" style="list-style:none">
      <li class="s1">BATHROOM REMODELING</li>
      <li class="s2">PLUMBING SERVICES</li>
      <li>DRAIN CLEANING</li>
    </ul>
    <div class="remodel__pipes" role="img" aria-label="Illustration of grey and yellow water pipes with valves"></div>
    <div class="remodel__photo" role="img" aria-label="Photo of a modern renovated bathroom with bathtub and vanity"></div>
    <svg class="remodel__wave" viewBox="0 0 267 90" preserveAspectRatio="none" aria-hidden="true">
      <path d="M0 30 Q130 70 267 10 L267 90 L0 90 Z" fill="var(--yellow)"/>
      <path d="M0 62 Q130 80 267 50 L267 90 L0 90 Z" fill="var(--deep)"/>
    </svg>
    <p class="remodel__emergency">Emergency<br>Service</p>
    <div class="badge247">24/7</div>
    <div class="remodel__mascot" role="img" aria-label="Illustration of the masked plumber mascot holding a wrench"></div>
    <p class="remodel__url">preuredbastanova-example.hr</p>
  </section>

  <!-- inside: services -->
  <section class="panel panel--services">
    <div class="services__band"><h2 class="services__title">Our full range<br>of plumbing services</h2></div>
    <div class="services__grid">
      <div class="service"><svg viewBox="0 0 30 30" fill="none" stroke="#fff" stroke-width="1.6"><path d="M6 4v10a9 9 0 0 0 18 0V4"/><path d="M15 24v3"/></svg>Leak Detection</div>
      <div class="service"><svg viewBox="0 0 30 30" fill="none" stroke="#fff" stroke-width="1.6"><rect x="4" y="6" width="10" height="8"/><path d="M4 14h20a8 8 0 0 1-16 6v6"/></svg>Toilet Repair<br>&amp; Installation</div>
      <div class="service"><svg viewBox="0 0 30 30" fill="none" stroke="#fff" stroke-width="1.6"><path d="M8 3v24M8 10h14v14"/><rect x="16" y="16" width="12" height="8"/></svg>Gas Lines</div>
      <div class="service"><svg viewBox="0 0 30 30" fill="none" stroke="#fff" stroke-width="1.6"><path d="M6 4v12a9 9 0 0 0 18 0V4"/><path d="M10 26h10"/></svg>Drain Cleaning</div>
      <div class="service"><svg viewBox="0 0 30 30" fill="none" stroke="#fff" stroke-width="1.6"><path d="M3 18h24M10 12h10v12H10z"/><path d="M15 4v8M11 4h8"/></svg>Gas Valves</div>
      <div class="service"><svg viewBox="0 0 30 30" fill="none" stroke="#fff" stroke-width="1.6"><path d="M8 3v14a7 7 0 0 0 14 0v-5h5"/></svg>Drain Repair</div>
      <div class="service"><svg viewBox="0 0 30 30" fill="none" stroke="#fff" stroke-width="1.6"><path d="M4 16h22v4a5 5 0 0 1-5 5H9a5 5 0 0 1-5-5z"/><path d="M8 16V6h5"/></svg>Shower Repair<br>&amp; Installation</div>
      <div class="service"><svg viewBox="0 0 30 30" fill="none" stroke="#fff" stroke-width="1.6"><path d="M4 6h22v6H18v14h-6V12H4z"/><path d="M15 17v3"/></svg>Burst Pipes</div>
      <div class="service"><svg viewBox="0 0 30 30" fill="none" stroke="#fff" stroke-width="1.6"><rect x="8" y="10" width="14" height="14"/><path d="M15 3v7M11 27h8"/></svg>Rooter<br>Services</div>
      <div class="service"><svg viewBox="0 0 30 30" fill="none" stroke="#fff" stroke-width="1.6"><rect x="3" y="12" width="24" height="12"/><path d="M6 12l4-6h10l4 6"/></svg>Garbage<br>Disposals</div>
      <div class="service"><svg viewBox="0 0 30 30" fill="none" stroke="#fff" stroke-width="1.6"><path d="M6 24L22 8M18 4l8 8"/><path d="M4 26l4-4"/></svg>Pipe Repair</div>
      <div class="service"><svg viewBox="0 0 30 30" fill="none" stroke="#fff" stroke-width="1.6"><path d="M4 16h14v-6M14 6h8"/><path d="M24 14v12M20 18h8"/></svg>Plumbing<br>Repairs</div>
      <div class="service" style="grid-column:1/2;margin-left:40px"><svg viewBox="0 0 30 30" fill="none" stroke="#fff" stroke-width="1.6"><rect x="7" y="3" width="16" height="22" rx="2"/><path d="M11 28v-3M19 28v-3M11 8h8"/></svg>Water Heaters</div>
      <div class="service" style="margin-left:40px"><svg viewBox="0 0 30 30" fill="none" stroke="#fff" stroke-width="1.6"><path d="M4 6h8v18h14"/><circle cx="21" cy="11" r="5"/><path d="M25 15l3 3"/></svg>Pipelining</div>
    </div>
    <div class="services__address">
      <svg width="16" height="20" viewBox="0 0 16 20" fill="none" stroke="#fff" stroke-width="1.6"><path d="M8 19s6-6.5 6-11A6 6 0 0 0 2 8c0 4.5 6 11 6 11z"/><circle cx="8" cy="8" r="2.2"/></svg>
      <span>48 Lindenfield Lane,<br>Brookhaven, State, 00000</span>
    </div>
  </section>

  <!-- front cover -->
  <section class="panel panel--cover">
    <div class="cover__lower"></div>
    <svg class="cover__swoosh" viewBox="0 0 267 120" preserveAspectRatio="none" aria-hidden="true">
      <path d="M0 80 Q120 10 267 20 L267 70 Q130 60 0 95 Z" fill="var(--yellow)"/>
      <path d="M0 95 Q130 60 267 70 L267 80 Q130 75 0 105 Z" fill="var(--red)"/>
      <path d="M0 105 Q130 75 267 80 L267 120 L0 120 Z" fill="var(--royal)"/>
    </svg>
    <div class="cover__mascot" role="img" aria-label="Illustration of the masked plumber mascot holding a pipe wrench"></div>
    <div class="cover__brand"><i></i>Vellmora</div>
    <h2 class="cover__tagline">Let the water<br><span>stay in the pipes</span> only.</h2>
    <p class="cover__intro">Adaptations of bathrooms and unclogging of drains in Zagreb and its surroundings.</p>
    <div class="cover__features">
      <span>Unclogging of<br>sewers &amp; drains</span><span class="sep"></span>
      <span>Pipe leak<br>detection</span><span class="sep"></span>
      <span>Change of<br>sanitary facilities</span>
    </div>
    <div class="cover__emergency">
      <svg class="cover__phone-icon" viewBox="0 0 30 40" fill="none" stroke="#fff" stroke-width="1.8"><rect x="3" y="2" width="22" height="36" rx="3"/><path d="M11 34h6"/><circle cx="18" cy="12" r="6"/></svg>
      <p class="label">EMERGENCY INTERVENTIONS</p>
      <p class="phone">095-410-2286</p>
    </div>
    <div class="cover__cta">CALL US NOW</div>
    <p class="cover__url">vellmora-example.hr</p>
  </section>

</main>
</body>
</html>
```